Business card Zottelgarten

Business card is for a self-employed dog trainer with own dog school. Name and logo of the dog school are available. Color specifications as well. The design should be classy and minimalist, but also modern. An already existing idea would be: Front: Only the logo Back: Contact data

Font styles to use
Serif
Sans Serif
Other font styles liked:
• Trajan Pro

Colors
f78f20

Requirements
Must have
• Name: Margit Wendler-Rasch Title: Dipl. Dog Trainer Contain my logo Follow my font and color preferences (see files)

```html
<!DOCTYPE html>
<html lang="en">
<head>
<meta charset="utf-8">
<title>Business card – Zottelgarten</title>
<link rel="stylesheet" href="https://fonts.googleapis.com/css2?family=Cinzel:wght@400;600&family=PT+Sans:wght@400;700&display=swap">
<style>
  :root {
    --stage: #2a2623;
    --card: #141414;
    --card-edge: #1d1d1d;
    --tan: #8d7862;
    --tan-name: #8f6d4a;
    --silver: #8a8a8a;
    --text: #e9e9e9;
    --rule: #9a9a9a;
  }
  * { margin: 0; padding: 0; box-sizing: border-box; }
  html, body { width: 1200px; height: 864px; overflow: hidden; }
  body {
    background: var(--stage);
    display: flex;
    align-items: center;
    justify-content: center;
    gap: 60px;
    font-family: "PT Sans", sans-serif;
  }
  .card {
    width: 510px;
    height: 330px;
    background: var(--card);
    border: 1px solid var(--card-edge);
    border-radius: 4px;
    box-shadow: 0 10px 30px rgba(0,0,0,.45);
    position: relative;
  }
  /* Front */
  .card-front {
    display: flex;
    align-items: center;
    justify-content: center;
  }
  .front-mark {
    display: flex;
    flex-direction: column;
    align-items: center;
    gap: 14px;
  }
  .mark-disc {
    width: 96px; height: 96px;
    border-radius: 50%;
    background: radial-gradient(circle at 40% 35%, #6a6a6a, #3a3a3a);
  }
  .front-name {
    font-family: "Cinzel", serif;
    font-weight: 400;
    font-size: 30px;
    letter-spacing: 2px;
    color: var(--silver);
  }
  /* Back */
  .card-back {
    display: flex;
    align-items: center;
    padding: 0 34px;
  }
  .back-mark {
    width: 170px;
    display: flex;
    flex-direction: column;
    align-items: center;
    gap: 12px;
  }
  .back-disc {
    width: 140px; height: 140px;
    border-radius: 50%;
    background: var(--tan);
    border: 2px solid var(--card);
    outline: 1.5px solid var(--tan);
  }
  .back-name {
    font-family: "Cinzel", serif;
    font-size: 15px;
    letter-spacing: 1px;
    color: var(--tan);
  }
  .divider {
    width: 1px;
    height: 190px;
    margin: 0 16px 0 26px;
    background: linear-gradient(to bottom, transparent, var(--rule) 20%, var(--rule) 80%, transparent);
  }
  .contact { color: var(--text); font-size: 15px; line-height: 1.22; }
  .person-name {
    font-weight: 700;
    font-size: 16px;
    letter-spacing: .5px;
    color: var(--tan-name);
    text-transform: uppercase;
  }
  .person-title { text-transform: uppercase; margin-bottom: 8px; }
  .address { margin-bottom: 6px; }
  .contact-list { list-style: none; }
  .contact-list li { display: flex; align-items: center; gap: 8px; }
  .contact-list svg { width: 11px; height: 11px; fill: #bdbdbd; flex: none; }
</style>
</head>
<body>
  <section class="card card-front" aria-label="Card front">
    <div class="front-mark">
      <div class="mark-disc"></div>
      <span class="front-name">ZOTTELGARTEN</span>
    </div>
  </section>

  <section class="card card-back" aria-label="Card back">
    <div class="back-mark">
      <div class="back-disc"></div>
      <span class="back-name">Zottelgarten</span>
    </div>
    <div class="divider"></div>
    <div class="contact">
      <p class="person-name">Margit Wendler-Rasch</p>
      <p class="person-title">Dipl. Dog Trainer</p>
      <p class="address">27 Lindenhof Lane<br>Brookvale, NY 12045</p>
      <ul class="contact-list">
        <li><svg viewBox="0 0 12 12"><path d="M1 4c0-2 2-3 5-3s5 1 5 3H8V3H4v1zM2 5h8l1 6H1z"/></svg>555 0142 7781</li>
        <li><svg viewBox="0 0 12 12"><path d="M3 0h6v12H3zM4 1v8h4V1z"/></svg>555 0196 3408</li>
        <li><svg viewBox="0 0 12 12"><path d="M3 0h6v4H3zM1 4h10v6H1zM3 8v4h6V8z"/></svg>555 0173 6254</li>
        <li><svg viewBox="0 0 12 12"><path d="M0 2h12v8H0zM1 3l5 4 5-4v-.2H1z"/></svg>info@zottelgarten.ch</li>
        <li><svg viewBox="0 0 12 12"><circle cx="6" cy="6" r="6"/></svg>www.zottelgarten.ch</li>
      </ul>
    </div>
  </section>
</body>
</html>
```